Chiropractic Business Card

I need a business card designed to help me stand apart from my competition. I really like simple, clean designs that appear open and inviting. I would like the designs to incorporate the color blue, green, or both. I really like the attached picture because it highlights that I just don't treat "back pain" and it being a nice computer graphic helps show that I have a modern practice. "Modern practice" meaning merging technology and most current research in my patient care.

My information is:

Wesley Marrin, DC
Phone- (707) 555-0182
Email- drwesleymarrin@example-mail.net
Website- www.pelhamchiropractic.example
Address- 248 Tolliver Street, Sonoma, CA 95476

Jpeg and pdf attached of Pelham Chiropractic logo.
Updates

Atmosphere to be clean lines and solid colors to be have gradient fading, but don't want too much going on with the fading. Simple.

Target Market(s)

Active adults who are health conscious between the ages of 20-70

Industry/Entity Type

Computer

Colors
0455a3
85cae6

Requirements
Must have
• Change color of Pelham chiropractic logo (maroon) to fit the rest of the design.
Nice to have
• Can separate the running image from the black background to have it work with the design.

```html
<!DOCTYPE html>
<html lang="en">
<head>
<meta charset="utf-8">
<title>Pelham Chiropractic – Business Card</title>
<link rel="stylesheet" href="https://fonts.googleapis.com/css2?family=Jost:wght@400;500;600&display=swap">
<style>
  :root {
    --page-bg: #e6e8ea;
    --card-white: #f3f3f3;
    --brand-blue: #0455a3;
    --brand-green: #5fa533;
    --grad-green: #4f9a3c;
    --grad-teal: #1f7f86;
    --grad-blue: #0b58a6;
    --text-dark: #3b3b3b;
    --text-mid: #5a5a5a;
  }
  * { box-sizing: border-box; margin: 0; padding: 0; }
  html, body {
    width: 1200px; height: 900px; overflow: hidden;
    background: var(--page-bg);
    font-family: "Jost", sans-serif;
  }
  .canvas { position: relative; width: 1200px; height: 900px; }
  .card {
    position: absolute; left: 337px;
    width: 525px; height: 300px;
    border-radius: 4px;
    box-shadow: 0 6px 18px rgba(0,0,0,0.18);
    overflow: hidden;
  }
  /* front */
  .card-front {
    top: 110px;
    background: linear-gradient(20deg, var(--grad-green) 0%, var(--grad-teal) 48%, var(--grad-blue) 100%);
  }
  .card-front .figure-art {
    position: absolute; left: 70px; top: 18px;
    width: 220px; height: 262px;
    border-radius: 46% 54% 40% 60% / 30% 38% 62% 70%;
    background: radial-gradient(ellipse at 50% 45%, rgba(169,198,214,0.75) 0%, rgba(120,170,190,0.35) 55%, rgba(120,170,190,0) 75%);
  }
  .card-front .brand-name {
    position: absolute; left: 300px; top: 150px;
    width: 200px;
    color: #ffffff;
    font-weight: 500; font-size: 28px; line-height: 1.08;
    letter-spacing: 0.4px;
  }
  /* back */
  .card-back { top: 490px; background: var(--card-white); }
  .card-back .brand-name {
    position: absolute; left: 34px; top: 34px;
    color: var(--brand-green);
    font-weight: 500; font-size: 28px; line-height: 1.05;
    letter-spacing: 0.4px;
  }
  .edge-band {
    position: absolute; left: 0; right: 0; bottom: 0; height: 10px;
    display: flex;
  }
  .edge-band .band-blue { width: 38%; background: var(--brand-blue); }
  .edge-band .band-green { flex: 1; background: var(--brand-green); }
  .contact {
    position: absolute; left: 200px; top: 110px; right: 18px;
    color: var(--text-mid);
    font-size: 10px; letter-spacing: 1.2px; text-transform: uppercase;
    white-space: nowrap;
  }
  .contact .person {
    font-weight: 600; font-size: 12px; letter-spacing: 2.6px;
    color: var(--text-dark); margin: 0 0 10px 24px;
  }
  .contact .address { line-height: 1.6; margin: 0 0 8px 24px; }
  .contact .row {
    display: flex; align-items: center; gap: 12px;
    height: 22px;
  }
  .contact .row svg { width: 12px; height: 12px; flex: none; }
</style>
</head>
<body>
<div class="canvas">

  <section class="card card-front">
    <div class="figure-art" role="img" aria-label="Translucent running figure illustration with highlighted joints"></div>
    <div class="brand-name">Pelham Chiropractic</div>
  </section>

  <section class="card card-back">
    <div class="brand-name">Pelham Chiropractic</div>

    <div class="contact">
      <div class="person">Wesley Marrin, DC</div>
      <div class="address">
        <div>Address: 248 Tolliver Street, Sonoma</div>
        <div>CA 95476</div>
      </div>
      <div class="row">
        <svg viewBox="0 0 12 12" aria-hidden="true"><rect x="0.5" y="0.5" width="11" height="11" rx="2" fill="var(--brand-blue)"/><path d="M3.5 3h1.5l.6 1.6-.9.7a5 5 0 0 0 2 2l.7-.9 1.6.6V8.5A1 1 0 0 1 8 9.5 5.5 5.5 0 0 1 2.5 4a1 1 0 0 1 1-1z" fill="#fff"/></svg>
        <span>(707) 555-0182</span>
      </div>
      <div class="row">
        <svg viewBox="0 0 12 12" aria-hidden="true"><rect x="0.5" y="0.5" width="11" height="11" rx="2" fill="var(--brand-blue)"/><rect x="2.5" y="3.5" width="7" height="5" fill="none" stroke="#fff" stroke-width="0.9"/><path d="M2.5 3.5 6 6.5l3.5-3" fill="none" stroke="#fff" stroke-width="0.9"/></svg>
        <span>drwesleymarrin@example-mail.net</span>
      </div>
      <div class="row">
        <svg viewBox="0 0 12 12" aria-hidden="true"><circle cx="6" cy="6" r="5.5" fill="var(--brand-blue)"/><circle cx="6" cy="6" r="3.4" fill="none" stroke="#fff" stroke-width="0.8"/><path d="M2.6 6h6.8M6 2.6c-1.6 2-1.6 4.8 0 6.8M6 2.6c1.6 2 1.6 4.8 0 6.8" fill="none" stroke="#fff" stroke-width="0.7"/></svg>
        <span>www.pelhamchiropractic.example</span>
      </div>
    </div>

    <div class="edge-band"><span class="band-blue"></span><span class="band-green"></span></div>
  </section>

</div>
</body>
</html>
```